Commercial Real Estate

We need a business card design for a new commercial real estate business that specializes in apartment building brokerage. Not individual units but the entire complex. We find and represent the owners existing buildings and well as new buyers for those buildings. The design should convey trust, integrity, knowledge and growth. It should be easily read.

Target Market(s)

40 to 65 years old

Industry/Entity Type

Real Estate

```html
<!DOCTYPE html>
<html lang="en">
<head>
<meta charset="utf-8">
<title>Larkridge Property Investments — Business Card</title>
<link rel="stylesheet" href="https://fonts.googleapis.com/css2?family=PT+Serif:wght@400;700&family=Lato:wght@400&display=swap">
<style>
  :root {
    --page-bg: #e9e6e2;
    --teal-light: #a3f2f2;
    --teal: #7fd3cf;
    --teal-deep: #6fc6c2;
    --accent-teal: #5cc1bd;
    --ink: #3d3d3d;
    --ink-soft: #5a6566;
    --card-white: #fbfbfb;
    --card-white-shade: #ececec;
  }
  html, body {
    margin: 0;
    padding: 0;
    width: 1200px;
    height: 800px;
    overflow: hidden;
    background: var(--page-bg);
  }
  .stage {
    width: 1200px;
    height: 800px;
    display: flex;
    align-items: center;
    justify-content: center;
  }
  .business-card {
    width: 840px;
    height: 480px;
    display: flex;
    box-shadow: 0 10px 30px rgba(0,0,0,0.18);
    overflow: hidden;
  }
  .brand-panel {
    width: 360px;
    background: linear-gradient(160deg, var(--teal-light) 0%, var(--teal) 55%, var(--teal-deep) 100%);
    display: flex;
    flex-direction: column;
    align-items: center;
    justify-content: flex-end;
    padding-bottom: 56px;
    box-sizing: border-box;
  }
  .brand-mark {
    display: flex;
    align-items: center;
    gap: 12px;
    margin-bottom: 18px;
  }
  .brand-dot {
    width: 22px;
    height: 22px;
    border-radius: 50%;
    background: var(--ink-soft);
  }
  .brand-name {
    font-family: "PT Serif", Georgia, serif;
    font-weight: 700;
    font-size: 40px;
    letter-spacing: 1px;
    color: var(--ink-soft);
  }
  .brand-tagline {
    font-family: "PT Serif", Georgia, serif;
    font-weight: 700;
    font-size: 17px;
    letter-spacing: 3px;
    color: var(--ink-soft);
    margin-bottom: 26px;
  }
  .office-address {
    font-family: "PT Serif", Georgia, serif;
    font-size: 18px;
    line-height: 1.4;
    color: var(--ink-soft);
    text-align: center;
    font-style: normal;
  }
  .contact-panel {
    flex: 1;
    background: linear-gradient(170deg, var(--card-white) 0%, var(--card-white) 55%, var(--card-white-shade) 100%);
    padding: 70px 52px 0 40px;
    box-sizing: border-box;
    text-align: right;
  }
  .person-name {
    font-family: "PT Serif", Georgia, serif;
    font-size: 34px;
    color: var(--accent-teal);
    margin: 0;
    line-height: 1.1;
  }
  .person-title {
    font-family: "Lato", Arial, sans-serif;
    font-size: 17px;
    color: var(--ink);
    margin: 4px 0 0;
  }
  .phone-lines {
    margin-top: 54px;
    font-family: "PT Serif", Georgia, serif;
    font-weight: 700;
    font-size: 25px;
    line-height: 1.35;
    color: var(--ink);
  }
  .web-lines {
    margin-top: 44px;
    font-family: "PT Serif", Georgia, serif;
    font-weight: 700;
    font-size: 19px;
    line-height: 1.45;
    color: var(--ink-soft);
  }
  .web-lines p, .phone-lines p { margin: 0; }
</style>
</head>
<body>
  <main class="stage">
    <article class="business-card">
      <section class="brand-panel">
        <div class="brand-mark">
          <span class="brand-dot"></span>
          <span class="brand-name">LARKRIDGE</span>
        </div>
        <div class="brand-tagline">Property Investments</div>
        <address class="office-address">18 Alder Street Suite 200<br>Denver, CO 80206</address>
      </section>
      <section class="contact-panel">
        <h1 class="person-name">Miles Hartwell</h1>
        <p class="person-title">Broker Associate</p>
        <div class="phone-lines">
          <p>Phone: 303-555-0148</p>
          <p>Fax: 720-555-0192</p>
        </div>
        <div class="web-lines">
          <p>Email: miles@larkridgerealty.com</p>
          <p>www.larkridgerealty.com</p>
        </div>
      </section>
    </article>
  </main>
</body>
</html>
```